A5 Patient Information Booklet (Chiropractic Clinic) 4-8 pages

Here’s a polished, professional rewrite of your full brief and content, with clearer structure, corrected language, and a premium tone:

---

**Project Title:** Premium Patient Information Brochure (Chiropractic & Wellness Clinic)

---

### **Overview**

We are a health and wellness clinic seeking a premium, high-end patient information brochure to provide following a patient’s initial consultation and first treatment.

The purpose of this booklet is to:

* Reinforce trust and professionalism
* Help patients understand what to expect next
* Encourage adherence to care recommendations
* Position the clinic as calm, expert-led, and results-driven

---

### **Format**

* 4–8 page booklet (A5 or similar size)
* Print-ready and digital versions required

---

### **Target Audience**

Patients who have just completed their initial consultation and may have begun treatment. They may already be experiencing physical or mental changes, so the brochure should guide, reassure, and educate them on what comes next.

---

### **Tone & Style**

* Premium, calm, and reassuring
* Modern wellness aesthetic (not overly clinical)
* Clean layout with minimal clutter
* Soft, neutral colour palette (whites, creams, muted greens, soft blues)
* Elegant typography (e.g. Montserrat / Lato)
* High-end, trustworthy, and professional feel

---

### **Key Messages**

#### 1. Listen to Your Body

Patients may feel different after treatment. Reassure them that this is normal and part of the healing process.

#### 2. Post-Treatment Advice

* Stay well hydrated
* Rest if needed
* Avoid overexertion if the body requires recovery

#### 3. Healing is a Journey (Core Concept)

A strong visual metaphor of a **“road to recovery”** or **journey** should be central to the design.

This journey should clearly illustrate three phases:

* **Phase 1: Initial Care (Weeks 1–6)**
Focus: Reducing pain/discomfort, calming the body, and initiating response to treatment

* **Phase 2: Corrective Care (Weeks 6–12)**
Focus: Addressing underlying issues, improving function, and creating lasting change

* **Phase 3: Wellness / Maintenance (Ongoing)**
Focus: Maintaining progress, preventing relapse, and supporting long-term wellbeing

**Important:**

* Emphasise that this is not a quick fix
* Progress requires time and consistency
* Each patient follows an individualised care plan
* The journey should feel structured, positive, and achievable

#### 4. Personalised Care

Reinforce that every treatment plan is tailored specifically to the individual.

#### 5. Professional Reassurance

Patients should feel confident they are in expert hands and supported throughout their journey.

---

### **Design Direction**

* Use imagery that reflects calmness, progression, and wellness (e.g. pathways, nature, soft gradients)
* Avoid generic stock imagery
* **Only use original clinic images from website and social media**
* Prioritise white space and clarity
* Aim for a luxury spa/medical hybrid aesthetic

---

## **Content Structure (Page-by-Page)**

### **Front Cover**

* Clean, minimal, premium design
* Clinic branding

---

### **Page 1: Patient Case Summary**

**Title:** *Welcome to Fernwell Practice*

Thank you for choosing Fernwell Practice.

This booklet is designed to guide you through:

* What we found during your initial consultation
* Your personalised recommended treatment plan
* Your road to recovery
* Long-term wellness care
* Why we take the approach we do

---

### **Page 2: Your Care Journey**

**Stage 1: Your Initial Consultation**

Today we completed a comprehensive assessment of your health and function, including:

* Full case history and discussion of your symptoms and goals
* Orthopaedic and neurological testing
* Postural and movement assessment
* Initial treatment (where appropriate)

**What this tells us:**

* How your body is currently functioning
* Where areas of stress or dysfunction may be present
* The most appropriate and effective path forward for your care

---

### **Page 3: Your Suggested Treatment Plan**

Based on today’s findings, your recommended care plan is:

**______ treatments over ______ weeks**

This should be viewed alongside your *Road to Recovery* to help you understand what to expect.

We have also discussed:

* Expected timelines for improvement
* Available payment options

**After Treatment:**
It is common to feel different following treatment. This is a normal response as your body begins to adapt and respond.

We recommend:

* Staying well hydrated
* Allowing time for rest and recovery
* Avoiding overexertion if your body feels it needs it

---

### **Page 4: What to Expect Next**

Healing is not always linear—it is a process that occurs over time.

Your care will typically progress through the following stages:

* **Relief Care**
Focused on reducing discomfort and calming the body

* **Corrective Care**
Focused on addressing underlying issues and improving function
(This phase may include prescribed exercises)

* **Maintenance / Wellness Care**
Focused on sustaining progress, preventing recurrence, and supporting long-term health

---

### **Page 5: Understanding Chiropractic Care**

**What is Chiropractic?**
Chiropractic care focuses on the relationship between the spine, nervous system, and overall body function.

By improving spinal movement and alignment, chiropractic care helps support the nervous system, allowing the body to function and heal more effectively.

**About Fernwell Practice**
At Fernwell Practice, our approach is centred around personalised, patient-focused care. We aim to not only relieve symptoms but to address underlying causes and support long-term wellbeing.

---

### **Back Page**

* Clinic contact details
* Website
* Social media icons/handles

**Closing Message:**
“A healthier, stronger you—supported every step of the way.”

---

### **Deliverables**

* Print-ready PDF
* Editable source files

---

### **Additional Notes**

* The brochure should feel valuable and worth keeping
* Encourage long-term care in a subtle, non-pushy way
* Maintain clarity, readability, and strong visual hierarchy
* Balance professionalism with warmth and approachability

---

If you’d like, I can also turn this into **actual brochure copy (fully written, patient-facing text)** or help you refine it further for a designer.

Target Market(s)

Existing patients who want to feel better and look after themselves that is given after their initil consultation appointment

Industry/Entity Type

Chiropractic, wellness, health

Font styles to use
Other font styles liked:
• Montserrat or Lato

Colors
0094D4
00A9DD
6FCCEA
C7EBF8
E9F6FB
00AB8E
00BBA5
67D7C9
C6EFE9
E9F9F6
6B429C
8869AF
B7A5CE
E3DAEB
F3F0F8

Requirements
Must have
• my own photos, look premium wellness, be clear and simple to understand for patients journey or what to expect next and over time
Nice to have
• USe my social media/website for ideas
Should not have
• generic photos and images

```html
<!DOCTYPE html>
<html lang="en">
<head>
<meta charset="utf-8">
<title>Fernwell Practice – Healing &amp; Wellness Guide</title>
<link href="https://fonts.googleapis.com/css2?family=Inter:wght@400;500;600;700&display=swap" rel="stylesheet">
<style>
  :root {
    --bg: #d6d6d6;
    --paper-back: #e4e4e4;
    --paper-front: #f7f7f7;
    --teal: #15a58b;
    --teal-bright: #1fbfae;
    --navy: #2e3d51;
    --text: #3a4555;
    --panel: #b1d5d0;
    --icon-bg: #bcdcd7;
    --line: #4a5563;
  }
  * { box-sizing: border-box; margin: 0; padding: 0; }
  html, body { width: 1200px; height: 840px; overflow: hidden; }
  body {
    background: var(--bg);
    font-family: "Inter", Arial, sans-serif;
    color: var(--text);
    display: flex;
    align-items: center;
    justify-content: center;
  }
  .spread { display: flex; width: 1022px; height: 780px; box-shadow: 0 20px 40px rgba(0,0,0,.18); }
  .page { position: relative; width: 511px; height: 780px; }

  /* Back page */
  .back { background: var(--paper-back); padding: 44px 40px 0 40px; }
  .section-title { font-size: 24px; font-weight: 600; color: var(--navy); letter-spacing: -.2px; }
  .section-title .accent { color: var(--teal); }
  .intro { margin-top: 14px; font-size: 12px; line-height: 1.5; }
  .plan-box {
    margin-top: 22px; background: var(--panel); border-radius: 14px;
    padding: 20px 20px 16px; font-size: 12px; color: var(--navy);
  }
  .plan-row { display: flex; align-items: flex-end; height: 22px; }
  .plan-row .fill { flex: 1; border-bottom: 1px solid var(--line); margin-left: 4px; height: 12px; }
  .plan-row .short { flex: 0 0 72px; border-bottom: 1px solid var(--line); margin: 0 4px; height: 12px; }
  .plan-row.blank .fill { margin-left: 0; }
  .plan-note { margin-top: 14px; font-size: 9.5px; font-weight: 500; }
  .support { margin-top: 44px; }
  .features { margin-top: 22px; display: grid; grid-template-columns: 1fr 1fr; row-gap: 20px; column-gap: 14px; }
  .feature { display: flex; align-items: center; gap: 14px; font-size: 12px; line-height: 1.45; }
  .feature-icon {
    flex: 0 0 44px; height: 44px; border-radius: 50%; background: var(--icon-bg);
    display: flex; align-items: center; justify-content: center;
  }
  .quote {
    margin-top: 44px; text-align: center; color: var(--teal);
    font-size: 17px; font-weight: 500; line-height: 1.55;
  }
  .back-footer { position: absolute; left: 40px; right: 30px; bottom: 48px; display: flex; align-items: center; gap: 22px; }
  .brand-mark { display: flex; flex-direction: column; align-items: center; gap: 6px; width: 92px; }
  .brand-dot { width: 46px; height: 46px; border-radius: 50%; background: var(--teal-bright); opacity: .85; }
  .brand-name { font-size: 11px; font-weight: 600; color: var(--navy); white-space: nowrap; }
  .contacts { font-size: 9.5px; color: var(--navy); line-height: 1.75; }
  .contacts li { list-style: none; display: flex; align-items: center; gap: 8px; }
  .contacts .social { margin-top: 4px; }
  .social-chip { width: 12px; height: 12px; background: var(--navy); border-radius: 2px; }

  /* Front cover */
  .front { background: var(--paper-front); overflow: hidden; }
  .cover-text { position: relative; z-index: 2; padding: 70px 0 0 44px; }
  .kicker { font-size: 26px; font-weight: 600; color: var(--teal-bright); }
  .headline { margin-top: 4px; font-size: 54px; font-weight: 700; color: var(--navy); line-height: 1.15; letter-spacing: -.5px; }
  .tagline { margin-top: 62px; font-size: 21px; font-weight: 500; color: var(--teal-bright); line-height: 1.6; }
  .cover-brand { position: absolute; z-index: 2; top: 72px; right: 38px; display: flex; flex-direction: column; align-items: center; gap: 8px; }
  .cover-brand .brand-dot { width: 62px; height: 62px; }
  .cover-brand .brand-name { font-size: 13px; }
  .cover-photo {
    position: absolute; left: 0; right: 0; bottom: 0; height: 440px;
    background: linear-gradient(180deg, #f7f7f7 0%, #ece8e3 18%, #ddd6cd 40%, #c9b49a 70%, #a98b6a 100%);
  }
</style>
</head>
<body>
<main class="spread">
  <section class="page back">
    <h2 class="section-title"><span class="accent">Your Personalised</span> Care Plan</h2>
    <p class="intro">Your body is unique. Your plan should be too. We’ve created a care plan tailored to your needs and goals.</p>

    <div class="plan-box">
      <div class="plan-row">Patient Name:<span class="fill"></span></div>
      <div class="plan-row">Your Suggested Care Plan:<span class="fill"></span></div>
      <div class="plan-row">Treatments over<span class="short"></span>weeks</div>
      <div class="plan-row">Notes:<span class="fill"></span></div>
      <div class="plan-row blank"><span class="fill"></span></div>
      <div class="plan-row blank"><span class="fill"></span></div>
      <p class="plan-note">*We will review your progress regularly and adjust your plan as you improve.</p>
    </div>

    <h2 class="section-title support"><span class="accent">We are here to</span> Support You</h2>
    <div class="features">
      <div class="feature">
        <span class="feature-icon"><svg width="22" height="22" viewBox="0 0 24 24" fill="none" stroke="#15a58b" stroke-width="1.6"><path d="M12 20s-7-4.5-7-10a4 4 0 0 1 7-2.5A4 4 0 0 1 19 10c0 5.5-7 10-7 10z"/></svg></span>
        <span>Expert care from qualified professionals.</span>
      </div>
      <div class="feature">
        <span class="feature-icon"><svg width="22" height="22" viewBox="0 0 24 24" fill="none" stroke="#15a58b" stroke-width="1.6"><rect x="5" y="3" width="13" height="18" rx="2"/><path d="M8 8h7M8 12h7M8 16h4"/></svg></span>
        <span>Personalised treatment just for you.</span>
      </div>
      <div class="feature">
        <span class="feature-icon"><svg width="22" height="22" viewBox="0 0 24 24" fill="none" stroke="#15a58b" stroke-width="1.6"><path d="M4 20h16M6 20v-5M10 20v-8M14 20v-6M18 20V8"/></svg></span>
        <span>Ongoing support at every stage.</span>
      </div>
      <div class="feature">
        <span class="feature-icon"><svg width="22" height="22" viewBox="0 0 24 24" fill="none" stroke="#15a58b" stroke-width="1.6"><path d="M12 3l2.6 5.3 5.9.9-4.3 4.1 1 5.8L12 16.3 6.8 19l1-5.8-4.3-4.1 5.9-.9z"/></svg></span>
        <span>Helping you move, feel and live better.</span>
      </div>
    </div>

    <p class="quote">“Your health is an investment in your future.<br>We’re here for the long run.”</p>

    <footer class="back-footer">
      <div class="brand-mark">
        <span class="brand-dot"></span>
        <span class="brand-name">Fernwell Practice</span>
      </div>
      <ul class="contacts">
        <li><svg width="10" height="10" viewBox="0 0 24 24" fill="none" stroke="#2e3d51" stroke-width="2"><path d="M12 22s7-7 7-12a7 7 0 0 0-14 0c0 5 7 12 7 12z"/><circle cx="12" cy="10" r="2.5"/></svg>12 Orchard Lane, Ashby Vale, Somerset, AV3 7KL, United Kingdom</li>
        <li><svg width="10" height="10" viewBox="0 0 24 24" fill="none" stroke="#2e3d51" stroke-width="2"><rect x="3" y="5" width="18" height="14"/><path d="M3 5l9 8 9-8"/></svg>Email: hello@fernwellpractice.co.uk</li>
        <li><svg width="10" height="10" viewBox="0 0 24 24" fill="none" stroke="#2e3d51" stroke-width="2"><circle cx="12" cy="12" r="9"/><path d="M3 12h18M12 3c3 3 3 15 0 18M12 3c-3 3-3 15 0 18"/></svg>Website: www.fernwellpractice.co.uk</li>
        <li class="social"><span class="social-chip"></span>fernwellpractice</li>
      </ul>
    </footer>
  </section>

  <section class="page front">
    <div class="cover-photo" role="img" aria-label="Photograph of a practitioner's hands treating the upper back of a patient lying face down in a white shirt"></div>
    <div class="cover-brand">
      <span class="brand-dot"></span>
      <span class="brand-name">Fernwell Practice</span>
    </div>
    <div class="cover-text">
      <p class="kicker">Your Guide to</p>
      <h1 class="headline">Healing &amp;<br>Wellness</h1>
      <p class="tagline">Personalised Care.<br>Real Results. Lasting Change.</p>
    </div>
  </section>
</main>
</body>
</html>
```